For our product portfolio we need a new packaging design. Our product is a Guaraná-derived energy in powder form. It is sold in small bags, between 350 x 400 mm and 700 x 800 mm, and also in boxes e.g. in the size of 240 x 160 x 45mm.

Our goal is to get creative product design which can be used for
a) the small bags,
b) the boxes, and
c) our Web site logo.

Target Market(s)

Our current target market are computer and Internet geeks. Therefore, we used a LOL-cat in our current/previous design. With the new design we would like to address a broader audience. It would be nice to see logos and packaging designs that are suitable to catch the attention of both geeks as well as normal folks.

Our target audience are people who would buy energy drinks or drink a lot of coffee.

The target audience are young people who work hard and/or go to parties and festivals. The design should be rather playful and funny than serious business.

Industry/Entity Type

Product

Requirements
Must have
• 1. A relationship to the nature product Guaraná. You could, for example, use the red fruits and green leaves of the guarana plant in the design to signal that the product is organic and good for your health. Take a look at http://en.plinthopedia.example/wiki/Guarana for inspirations.
• 2. Our product name is "Velora Fizzpulver"
• 3. The small bags must have certain information in multiple languages (please see image attached as file 1 for reference). We will tell you the specifics when your design is selected as one of our favorites. However, please keep some space in your packaging design for the information text.
• 4. The boxes must have certain information in multiple languages (please see image attached as file 3 for reference). We will tell you the specifics when your design is selected as one of our favorites.
• 5. The graphics must be delivered in an open format so that we can make changes and adjustments after the competition has finished.
• 6. The graphics for packaging must use CMYK colors with at least 600dpi. The logo must use RGB colors with 72dpi.
• Please avoid resemblance with other trademarks, such as Tovimba Borealis.
Nice to have
• A brand identity that is appealing to the "Internet community", e.g. a LOL-cat animal, an Internet meme, or the like.
• Another idea would be to use a hybrid animal, such as http://www.snipmorphs.example/gallery/data/418/medium/stretch_snipmorphs.jpg
• In any case, creative and imaginative submissions are preferred over boring submissions. We are open to all ideas.

```html
<!DOCTYPE html>
<html lang="en">
<head>
<meta charset="utf-8">
<title>Velora Fizzpulver – Sachet Front</title>
<link rel="stylesheet" href="https://fonts.googleapis.com/css2?family=Open+Sans:wght@600;700&display=swap">
<style>
  :root {
    --backdrop: #0b0a10;
    --backdrop-glow: #2a1e1a;
    --hazard-yellow: #f2c21b;
    --hazard-black: #2b2924;
    --leaf-green: #3f9a3a;
    --fruit-red: #d8322a;
    --label-white: #ffffff;
    --ink: #24211d;
    --tagline: #f7f4ec;
  }
  html, body {
    margin: 0;
    width: 1200px;
    height: 1200px;
    overflow: hidden;
  }
  body {
    background: radial-gradient(circle at 50% 55%, var(--backdrop-glow) 0%, var(--backdrop) 62%);
    font-family: "Open Sans", Arial, sans-serif;
    position: relative;
  }
  .sachet {
    position: absolute;
    left: 290px;
    top: 210px;
    width: 620px;
    height: 780px;
    overflow: hidden;
    border-radius: 10px;
    background: repeating-linear-gradient(
      -55deg,
      var(--hazard-black) 0 95px,
      var(--hazard-yellow) 95px 190px
    );
    box-shadow: 0 20px 50px rgba(0,0,0,0.6);
  }
  .sachet__seal {
    position: absolute;
    top: 0;
    bottom: 0;
    width: 26px;
    background: repeating-linear-gradient(
      90deg,
      rgba(255,255,255,0.12) 0 3px,
      rgba(0,0,0,0.06) 3px 6px
    );
  }
  .sachet__seal--left { left: 0; }
  .sachet__seal--right { right: 0; }
  .leaf-band {
    position: absolute;
    left: 0;
    right: 0;
    height: 22px;
    background: var(--leaf-green);
  }
  .leaf-band--top { top: 0; }
  .leaf-band--bottom { bottom: 0; }
  .brand-label {
    position: absolute;
    left: 50%;
    top: 330px;
    transform: translateX(-50%);
    display: flex;
    align-items: center;
    gap: 18px;
    background: var(--label-white);
    border-radius: 60px;
    padding: 20px 40px 20px 26px;
    white-space: nowrap;
    box-shadow: 0 0 0 6px var(--leaf-green);
  }
  .fruit-dot {
    width: 46px;
    height: 46px;
    border-radius: 50%;
    background: var(--fruit-red);
    flex: none;
  }
  .brand-name {
    margin: 0;
    font-weight: 700;
    font-size: 46px;
    line-height: 1;
    color: var(--ink);
    letter-spacing: 0.5px;
  }
  .tagline {
    position: absolute;
    left: 0;
    right: 0;
    top: 630px;
    text-align: center;
    color: var(--tagline);
    font-weight: 700;
    font-size: 15px;
    letter-spacing: 6px;
    line-height: 1.8;
    text-transform: uppercase;
    text-shadow: 0 1px 3px rgba(0,0,0,0.7);
  }
  .tagline p { margin: 0; }
</style>
</head>
<body>
  <main class="sachet">
    <div class="sachet__seal sachet__seal--left"></div>
    <div class="sachet__seal sachet__seal--right"></div>
    <div class="leaf-band leaf-band--top"></div>
    <div class="leaf-band leaf-band--bottom"></div>
    <div class="brand-label">
      <span class="fruit-dot"></span>
      <h1 class="brand-name">Velora Fizzpulver</h1>
    </div>
    <div class="tagline">
      <p>Refuel. Recharge.</p>
      <p>Energy in powder form</p>
    </div>
  </main>
</body>
</html>
```